uk based ecommerce website requires fresh look ,high quality look and feel

we are a web based company selling eco friendly ground reinforcement grids to diy and construction sectors
our existing website is www.plumbrookpaving.co.uk ,

we have already updated the logo so that is the branding sorted .so we need a ecommerce website that is very much up-to date in design and layout and which has content management system for ease of use so that we can add products and information as required.

Use current logo as reference for colour scheme.
www.plumbrookpaving.co.uk

The current website has 6 pages accessible through the navigation bar, I would now like 5 pages, removing the need for the Trade Enquiries page possibly have it with along with contact us.

Target Market(s)

construction industry , diy end users,
retail market, landscapers, gardeners

Industry/Entity Type

Construction

Font styles to use
Other font styles liked:
• logo font prometo

Colors
f78f20
9bcb3c

Requirements
Must have
• logo colours and logo design in website with cms responsive design for tablet and mobile devices
• expect content to work flawlessly and look great across all devices
• HTML 5 custom design with coding as required
• must have good experiance in ecommerce website design
• eye catching, high quality look and feel and very user friedly ,very up-to date.
Nice to have
• picture slider show
• explain in writing what exactly i am getting in my ecommerce website
Should not have
• plain , basic design , old fashion looking ,cheap look

```html
<!DOCTYPE html>
<html lang="en">
<head>
<meta charset="utf-8">
<title>Plumbrook Paving – Ground Solutions</title>
<link href="https://fonts.googleapis.com/css2?family=Oswald:wght@300;400&family=Roboto:wght@500&family=Open+Sans:wght@400;600&display=swap" rel="stylesheet">
<style>
:root{
  --orange:#f78f20;
  --green:#5d9e3a;
  --green-band:#5a9c3c;
  --green-btn:#4f8f30;
  --ink:#222;
  --muted:#555;
  --pale:#f4f4f4;
  --pale-2:#ececec;
  --white:#fff;
}
*{box-sizing:border-box;margin:0;padding:0}
html,body{width:694px;height:1200px;overflow:hidden}
body{position:relative;font-family:"Open Sans",Arial,sans-serif;color:var(--ink);background:var(--white)}
.abs{position:absolute}
.heading{font-family:"Oswald",sans-serif;font-weight:300;text-align:center;color:var(--ink);letter-spacing:.3px;line-height:1}
.diamond{width:7px;height:7px;background:var(--green);transform:rotate(45deg)}
.btn{display:flex;align-items:center;justify-content:center;background:var(--green);color:var(--white);font-size:6px;text-transform:uppercase}

/* hero */
.hero{left:0;top:0;width:694px;height:278px;background:linear-gradient(180deg,#3b3d33 0%,#4a5a3a 45%,#6f7060 70%,#2f4424 100%)}
.hero-panel{left:152px;top:98px;width:384px;height:72px;background:rgba(30,30,30,.72);text-align:center;padding-top:18px}
.hero-title{font-family:"Roboto",sans-serif;font-weight:500;font-size:18px;line-height:1.1;color:var(--white)}
.hero-title span{color:var(--orange)}
.hero-sub{font-size:5.6px;color:#eee;width:260px;margin:4px auto 0;line-height:1.3}
.hero-btn{left:314px;top:179px;width:88px;height:18px;background:var(--orange);color:var(--white);font-size:7px;display:flex;align-items:center;justify-content:center}

/* nav */
.nav{left:0;top:278px;width:694px;height:32px;background:linear-gradient(#fff,#f2f2f2)}
.brand{left:108px;top:286px;display:flex;align-items:center;gap:4px}
.brand-mark{width:16px;height:16px;border-radius:50%;background:var(--green)}
.brand-name{font-weight:600;font-size:7px;color:var(--orange);line-height:1.1}
.menu{right:120px;top:291px;display:flex;font-size:5.2px;color:#333;text-transform:uppercase;line-height:1.2}
.menu li{list-style:none;padding:0 7px;border-left:1px solid #ccc}
.menu li:first-child{border-left:0;padding-left:0}
.menu li:last-child{padding-right:0}
.menu li.active{color:var(--orange)}

/* welcome */
.welcome{left:0;top:310px;width:694px;height:186px;background:var(--pale)}
.welcome .heading{top:34px;width:694px;font-size:20px}
.welcome .diamond{left:339px;top:57px}
.about{left:104px;top:93px;width:266px}
.about h2{font-weight:400;font-size:9px;line-height:1.2;color:#111}
.about h3{font-size:5px;font-weight:400;margin:3px 0 4px 1px}
.about p{font-size:4.6px;line-height:1.55;color:var(--muted)}
.about-btn{left:103px;top:158px;width:82px;height:15px}
.about-photo{left:387px;top:72px;width:189px;height:101px;background:linear-gradient(160deg,#6a8f45,#b9ae92 55%,#8a8d86);border:1px solid #ccc}

/* products */
.products{left:0;top:496px;width:694px;height:246px;background:var(--pale-2)}
.products .heading{top:34px;width:694px;font-size:20px}
.products .diamond{left:339px;top:59px}
.card{top:78px;width:151px;height:149px;background:var(--white);text-align:center}
.card-photo{width:151px;height:71px;background:linear-gradient(160deg,#4c6b36,#7d7a6a 60%,#2c2c2c)}
.card .diamond{position:absolute;left:71px;top:66px;width:9px;height:9px}
.card h4{font-family:"Oswald",sans-serif;font-weight:300;font-size:8px;line-height:1.2;margin-top:10px;color:#333}
.card p{font-size:4.4px;line-height:1.5;color:var(--muted);padding:3px 5px 0}
.card .btn{position:absolute;left:46px;top:123px;width:56px;height:14px;text-transform:none;font-size:5.5px}

/* testimonials */
.clients{left:0;top:742px;width:694px;height:212px;background:var(--green-band)}
.clients .heading{top:16px;width:694px;font-size:20px;color:var(--white)}
.rule{left:312px;top:44px;width:70px;height:1px;background:#d7e9c8}
.clients .diamond{left:344px;top:41px;background:var(--white)}
.people{left:84px;top:46px;width:212px;height:166px;background:linear-gradient(90deg,#d9cfc4 0%,#8f8478 35%,#2b3450 60%,#3a4563 100%);border-radius:80px 80px 0 0}
.quote{left:311px;top:71px;width:264px;color:var(--white)}
.quote h3{font-family:"Oswald",sans-serif;font-weight:300;font-size:11px;line-height:1.2}
.quote p{font-size:4.7px;line-height:1.5;margin-top:6px;color:#eef5e8}
.clients-btn{left:311px;top:171px;width:82px;height:17px;background:var(--green-btn);text-transform:none}

/* contact */
.contact{left:0;top:954px;width:694px;height:246px;background:linear-gradient(90deg,#141414,#262626 50%,#1a1a1a)}
.contact .heading{top:20px;width:694px;font-size:20px;color:var(--white)}
.field{left:104px;width:230px;height:16px;background:#121212;border-bottom:1px solid #333;color:#ddd;font-size:5px;padding:5px 4px;line-height:1}
.field.comments{height:80px}
.submit{left:246px;top:206px;width:88px;height:15px;background:var(--green);color:var(--white);font-size:6px;display:flex;align-items:center;justify-content:center}
.info{left:348px;top:97px;width:220px;color:#ddd}
.info h4{font-weight:400;font-size:9px;line-height:1.2;color:var(--white)}
.info p{font-size:5px;line-height:1.45;margin-top:3px}
.info ul{list-style:none;margin-top:7px}
.info li{display:flex;align-items:center;gap:8px;font-size:5.6px;height:13px}
.info svg{width:7px;height:7px;fill:#888}
.social{left:350px;top:179px;display:flex;gap:2px}
.social span{width:17px;height:17px;background:#4a4a4a}
.social span.on{background:var(--green)}
.copyright{left:0;top:235px;width:694px;text-align:center;font-size:4.6px;color:#999}
</style>
</head>
<body>

<section class="abs hero" role="img" aria-label="Photo of a modern glass pavilion beside a gravel garden path at dusk"></section>
<div class="abs hero-panel">
  <h1 class="hero-title"><span>STONEMESH</span> MAKES WALKING ON IT EASY</h1>
  <p class="hero-sub">There are many variations of passages of Lorem Ipsum available, but the majority have suffered alteration in some form.</p>
</div>
<div class="abs hero-btn">Get Started</div>

<header class="abs nav"></header>
<div class="abs brand"><span class="brand-mark"></span><span class="brand-name">PLUMBROOK</span></div>
<ul class="abs menu">
  <li>Shop</li><li class="active">About Us</li><li>Ground Solutions</li><li>Plumbrook</li><li>Contact Us</li>
</ul>

<section class="abs welcome">
  <h2 class="abs heading">WELOCME TO PLUMBROOK</h2>
  <div class="abs diamond"></div>
  <div class="abs about">
    <h2>CONTAINED GRAVEL FOR PARKING AND PATHWAYS</h2>
    <h3>AFFORDABLE AND GREEN SOLUTIONS FOR FLOOD PREVENTION</h3>
    <p>PLUMBROOK is a family run company that specialises in stabilisation grid systems for gravel and grass surfaces. Our main focus is to provide Quality products at an affordable price and which meets the requirements of our customers. We supply a permeable paving system that keeps the traditional look of a gravel driveway, but gives it the more advanced and ecological approach of a contained gravel system All installations of all landscaping of driveways projects require to incorporate the SUDS techniques which is Sustainable Urban Drainage Systems.</p>
  </div>
  <div class="abs btn about-btn">Read More</div>
  <div class="abs about-photo" role="img" aria-label="Photo of a gravel garden with box hedges and a paved path"></div>
</section>

<section class="abs products">
  <h2 class="abs heading">PRODUCTS</h2>
  <div class="abs diamond"></div>
  <article class="abs card" style="left:103px">
    <div class="card-photo" role="img" aria-label="Photo of black ground grids laid beside a flower bed"></div>
    <div class="diamond"></div>
    <h4>CONTRARY TO POPULAR BELIEF</h4>
    <p>There are many variations of passages of Lorem Ipsum available, but the majority have suffered alteration in some form, by injected humour, or randomised words which don't</p>
    <div class="btn">Read More</div>
  </article>
  <article class="abs card" style="left:265px">
    <div class="card-photo" role="img" aria-label="Photo of a worker raking gravel into ground grids"></div>
    <div class="diamond"></div>
    <h4>CONTRARY TO POPULAR BELIEF</h4>
    <p>There are many variations of passages of Lorem Ipsum available, but the majority have suffered alteration in some form, by injected humour, or randomised words which don't</p>
    <div class="btn">Read More</div>
  </article>
  <article class="abs card" style="left:426px">
    <div class="card-photo" role="img" aria-label="Photo of a gravel garden with box hedges"></div>
    <div class="diamond"></div>
    <h4>CONTRARY TO POPULAR BELIEF</h4>
    <p>There are many variations of passages of Lorem Ipsum available, but the majority have suffered alteration in some form, by injected humour, or randomised words which don't</p>
    <div class="btn">Read More</div>
  </article>
</section>

<section class="abs clients">
  <h2 class="abs heading">OUR CLIENT SAY'S</h2>
  <div class="abs rule"></div>
  <div class="abs diamond"></div>
  <div class="abs people" role="img" aria-label="Photo of two business clients, a woman and a man drinking coffee"></div>
  <div class="abs quote">
    <h3>Contrary to popular belief,</h3>
    <p>There are many variations of passages of Lorem Ipsum available, but the majority have suffered alteration in some form, by injected humour, or randomised words which don't look even slightly believable. If you are going to use a passage of Lorem Ipsum, you need to be sure there isn't anything embarrassing hidden in the middle of text.</p>
    <p>It is a long established fact that a reader will be distracted by the readable content of a page when looking at its layout. The point of using Lorem Ipsum is that it has a more-or-less normal distribution of letters, as opposed to using 'Content here, content here', making it look like readable English. Many desktop publishing packages and web page editors now use Lorem Ipsum as their default model text, and a search for 'lorem ipsum' will uncover many web sites still in their infancy.</p>
  </div>
  <div class="abs btn clients-btn">Read More</div>
</section>

<footer class="abs contact">
  <h2 class="abs heading">GET IN TOUCH</h2>
  <div class="abs field" style="top:65px">Name:</div>
  <div class="abs field" style="top:84px">Phone:</div>
  <div class="abs field" style="top:103px">Email:</div>
  <div class="abs field comments" style="top:122px">Comments:</div>
  <div class="abs submit">Submit</div>
  <div class="abs info">
    <h4>Contact Info</h4>
    <p>There are many variations of passages of Lorem Ipsum available, but the majority have suffered alteration in some form, by injected humour, or randomised words which don't look even slightly believable.</p>
    <ul>
      <li><svg viewBox="0 0 10 10"><path d="M5 0a3.5 3.5 0 0 0-3.5 3.5C1.5 6 5 10 5 10s3.5-4 3.5-6.5A3.5 3.5 0 0 0 5 0zm0 5a1.5 1.5 0 1 1 0-3 1.5 1.5 0 0 1 0 3z"/></svg>Address: 14 Orchard Lane, Leeds, UK</li>
      <li><svg viewBox="0 0 10 10"><path d="M0 2h10v6H0zM0 2l5 3.5L10 2" stroke="#1d1d1d" stroke-width=".8"/></svg>Email: info@plumbrookpaving.co.uk</li>
      <li><svg viewBox="0 0 10 10"><path d="M2 0l2 2.5-1 1.2c.6 1.3 1.6 2.3 2.9 2.9l1.2-1L10 7.6 8.5 10C4 9.6.4 6 0 1.5z"/></svg>Call: 0113 496 0274</li>
    </ul>
  </div>
  <div class="abs social"><span></span><span></span><span class="on"></span><span></span></div>
  <p class="abs copyright">© 2016 PLUMBROOK PAVING LTD. All Right Reserved</p>
</footer>

</body>
</html>
```